Corvella Sign

Design a sign for Pizza and Pasta restaurant in New Jersey
Black background
Size = 120" w x 23.5" h
Corvella - top line
Brick Oven Pizza & Pasta - second line

Target Market(s)

everybody

Industry/Entity Type

restaurant

Font styles to use
Decorative
Script

Colors

Designer to choose only greyscale colors for use in the design.

Requirements
Must have
• Brick Oven Pizza & Pasta
Nice to have
• Vector file

```html
<!DOCTYPE html>
<html lang="en">
<head>
<meta charset="UTF-8">
<title>Corvella Sign</title>
<link href="https://fonts.googleapis.com/css2?family=Allura&family=Cinzel:wght@400&display=swap" rel="stylesheet">
<style>
  :root {
    --page: #e9e9e7;
    --sign: #0d0d0d;
    --ink: #f2f2f2;
    --rule: #bdbdbd;
    --art-light: #6a6a6a;
    --art-dark: #2a2a2a;
  }
  * { margin: 0; padding: 0; box-sizing: border-box; }
  html, body {
    width: 1200px;
    height: 799px;
    overflow: hidden;
    background: var(--page);
  }
  .canvas {
    position: relative;
    width: 1200px;
    height: 799px;
  }
  .sign {
    position: absolute;
    left: 50px;
    top: 292px;
    width: 1100px;
    height: 215px;
    background: var(--sign);
    overflow: hidden;
  }
  .sign__frame {
    position: absolute;
    inset: 0;
    width: 100%;
    height: 100%;
  }
  .art-pizza {
    position: absolute;
    left: 14px;
    top: 44px;
    width: 150px;
    height: 150px;
    border-radius: 50%;
    background: radial-gradient(circle at 50% 50%, var(--art-light), var(--art-dark) 72%);
  }
  .art-pasta {
    position: absolute;
    right: 14px;
    top: 12px;
    width: 265px;
    height: 140px;
    background: linear-gradient(135deg, var(--art-light), var(--art-dark));
  }
  .brand {
    position: absolute;
    left: 205px;
    top: 22px;
    width: 560px;
    text-align: center;
    font-family: "Allura", cursive;
    font-size: 128px;
    font-weight: 400;
    line-height: 1;
    color: var(--ink);
  }
  .tagline {
    position: absolute;
    top: 150px;
    height: 30px;
    font-family: "Cinzel", serif;
    font-size: 24px;
    line-height: 30px;
    letter-spacing: 3px;
    color: var(--ink);
    white-space: nowrap;
  }
  .tagline--oven { left: 210px; }
  .tagline--menu { left: 560px; }
</style>
</head>
<body>
<main class="canvas">
  <section class="sign" aria-label="Corvella brick oven pizza and pasta sign">
    <svg class="sign__frame" viewBox="0 0 1100 215" aria-hidden="true">
      <line x1="250" y1="20" x2="800" y2="20" stroke="var(--rule)" stroke-width="1.5"/>
      <line x1="210" y1="196" x2="1070" y2="196" stroke="var(--rule)" stroke-width="1.5"/>
      <line x1="1070" y1="162" x2="1070" y2="196" stroke="var(--rule)" stroke-width="1.5"/>
    </svg>
    <div class="art-pizza" role="img" aria-label="Line sketch of a sliced pizza"></div>
    <div class="art-pasta" role="img" aria-label="Line sketches of assorted pasta shapes"></div>
    <h1 class="brand">Corvella</h1>
    <p class="tagline tagline--oven">Brick Oven</p>
    <p class="tagline tagline--menu">Pizza &amp; Pasta</p>
  </section>
</main>
</body>
</html>
```